Summit Relay Business Card

Side 1: Summit Relay Logo (logo without Maltese cross) with industrial rope rescue related theme. Our company services - TRAINING - Fire Training, Confined Space Rescue Training, Rope Rescue training, Hazmat Training, Incident Command, EMS, Pump Operations Training. Website - summitrelay-example.com.
Side 2: Summit Relay Fire Department Logo (logo with Maltese cross) with Firefighter related theme. Company (division) services - FIELD SERVICES - Fire Department, Stand-by Rescue, Safety, EMS, Planning. "Supporting the Emergency Response Community Since 1967"

Add contact information wherever it makes since (Name, Email, Phone).
I would like it to represent the Summit Relay Fire Department Logo as a division not as a separate entity without saying it, possibly by depicting it in the background of Side 2 instead of being a standalone picture like the logo on Side 1.

```html
<!DOCTYPE html>
<html lang="en">
<head>
<meta charset="utf-8">
<title>Summit Relay Business Card</title>
<link rel="stylesheet" href="https://fonts.googleapis.com/css2?family=Montserrat:wght@400;500;600;700;800&display=swap">
<style>
  :root {
    --bg: #e8e8e9;
    --card-dark: #1f1f1f;
    --card-light: #fbfbfb;
    --red: #d6373d;
    --white: #ffffff;
    --ink: #2b2b2b;
    --muted: #d9d9d9;
  }
  * { box-sizing: border-box; margin: 0; padding: 0; }
  html, body { width: 1200px; height: 900px; overflow: hidden; }
  body {
    background: var(--bg);
    font-family: "Montserrat", sans-serif;
    position: relative;
  }
  .card {
    position: absolute;
    top: 296px;
    width: 540px;
    height: 309px;
    border-radius: 4px;
    overflow: hidden;
    background: var(--card-dark);
    box-shadow: 0 14px 30px rgba(0,0,0,0.22);
  }
  .card--services { left: 40px; }
  .card--contact { left: 620px; }

  /* Side 1 */
  .brand-block {
    position: absolute;
    top: 52px;
    left: 0;
    width: 100%;
    display: flex;
    align-items: center;
    justify-content: center;
    gap: 16px;
  }
  .brand-rule { width: 70px; height: 3px; background: var(--red); }
  .brand-name {
    font-weight: 800;
    font-size: 36px;
    letter-spacing: 1px;
    color: var(--red);
    line-height: 1;
  }
  .service-list {
    position: absolute;
    top: 140px;
    left: 150px;
    list-style: none;
    color: var(--white);
    font-size: 10.5px;
    font-weight: 500;
    letter-spacing: 0.4px;
    text-transform: uppercase;
    line-height: 20px;
  }
  .service-list li::before {
    content: "";
    display: inline-block;
    width: 5px; height: 5px;
    border-radius: 50%;
    background: var(--white);
    margin-right: 10px;
    vertical-align: middle;
    position: relative;
    top: -1px;
  }

  /* Side 2 */
  .card-shape { position: absolute; inset: 0; }
  .contact-block {
    position: absolute;
    left: 34px;
    top: 40px;
    color: var(--white);
  }
  .person-name { font-size: 19px; font-weight: 700; letter-spacing: 0.3px; }
  .person-title { font-size: 12.5px; font-weight: 400; margin-top: 2px; color: var(--muted); }
  .divider { width: 110px; height: 1px; background: var(--white); margin: 10px 0 10px; }
  .contact-line { font-size: 12.5px; line-height: 20px; color: var(--muted); }
  .division-label { font-size: 12.5px; font-weight: 700; margin-top: 10px; letter-spacing: 0.3px; }
  .division-services { font-size: 12px; line-height: 18px; color: var(--muted); margin-top: 2px; }

  .division-brand {
    position: absolute;
    left: 318px;
    top: 70px;
    width: 206px;
    text-align: center;
    color: var(--ink);
  }
  .division-mark {
    display: flex; align-items: center; justify-content: center; gap: 8px;
  }
  .division-dot { width: 16px; height: 16px; border-radius: 50%; background: var(--red); }
  .division-name { font-size: 20px; font-weight: 600; letter-spacing: 2.5px; color: var(--ink); }
  .division-rule { height: 2px; background: var(--red); margin: 10px auto 12px; width: 170px; }
  .tagline { font-size: 11.5px; font-weight: 500; line-height: 16px; color: var(--ink); }
</style>
</head>
<body>

<section class="card card--services" aria-label="Card side one: training services">
  <div class="brand-block">
    <span class="brand-rule"></span>
    <span class="brand-name">SUMMIT RELAY</span>
    <span class="brand-rule"></span>
  </div>
  <ul class="service-list">
    <li>Fire Training</li>
    <li>Confined Space Rescue Training</li>
    <li>Rope Rescue Training</li>
    <li>Hazmat Training</li>
    <li>Incident Command</li>
    <li>EMS &amp; Pump Operations Training</li>
  </ul>
</section>

<section class="card card--contact" aria-label="Card side two: contact and field services">
  <svg class="card-shape" width="540" height="309" viewBox="0 0 540 309" aria-hidden="true">
    <path d="M336 0 C 268 70, 268 239, 336 309 L540 309 L540 0 Z" fill="var(--red)"/>
    <path d="M350 0 C 284 70, 284 239, 350 309 L540 309 L540 0 Z" fill="var(--card-light)"/>
  </svg>

  <div class="contact-block">
    <div class="person-name">YOUR NAME</div>
    <div class="person-title">Your Title</div>
    <div class="divider"></div>
    <div class="contact-line">012-345-6789</div>
    <div class="contact-line">yourmail@summitrelay-example.com</div>
    <div class="contact-line">www.summitrelay-example.com</div>
    <div class="division-label">FIELD SERVICES</div>
    <div class="division-services">Fire Department, Stand-by Rescue<br>Safety, EMS, Planning.</div>
  </div>

  <div class="division-brand">
    <div class="division-mark">
      <span class="division-dot"></span>
      <span class="division-name">SUMMIT RELAY</span>
    </div>
    <div class="division-rule"></div>
    <p class="tagline">“ Supporting the Emergency<br>Response Community Since 1967 ”</p>
  </div>
</section>

</body>
</html>
```